Financial Advisor / Asset Manager Wix Design

I'm currently hosting with Wix and my first attempt at a website is live at www.bramwellhollowgroup.com Clearly I am not a web designer and I need help making this more catchy, modern, cross-platform compatible, search engine optimized, etc. I've got logos, hex color pallets, and a slew of other graphics. I'm interested in working with a winning designer to write/refine my copy/language to complete the build.

Full set of graphics https://albums.picnestly.io/r83Kd27WQfa5T1mZC do NOT use the CONSULTING graphics as this is for a related business / different website

Target Market(s)

Individuals, small institutions, endowments, non-profits seeking financial advice and asset / portfolio management

Industry/Entity Type

Financial Services

Coding

Coded - Design and coding required

Font styles to use
Other font styles liked:
• AvenirLTStd - Black, Book, and Roman as appropriate

Requirements
Must have
• Complete, cross platform website integrating my existing logo
Nice to have
• Easy to update format for go-forward maintenance

```html
<!DOCTYPE html>
<html lang="en">
<head>
<meta charset="utf-8">
<title>Bramwell Hollow Group</title>
<link rel="stylesheet" href="https://fonts.googleapis.com/css2?family=Nunito+Sans:wght@300;400;600;700;800;900&display=swap">
<style>
:root{
  --blue:#1b74c9;
  --blue-deep:#0d5fb3;
  --ink:#1d2733;
  --text:#4a5360;
  --muted:#8a939e;
  --line:#c9d6e3;
  --white:#ffffff;
  --black:#050607;
}
*{box-sizing:border-box;margin:0;padding:0}
html,body{width:1200px;height:4515px;overflow:hidden}
body{font-family:"Nunito Sans",Arial,sans-serif;color:var(--text);background:var(--white);position:relative}
.abs{position:absolute}
.btn{position:absolute;display:flex;align-items:center;justify-content:center;border:2px solid var(--blue);color:var(--blue);font-weight:800;font-size:14px;letter-spacing:.5px;background:var(--white)}

/* hero */
.hero{position:absolute;left:0;top:0;width:1200px;height:650px}
.hero-photo{position:absolute;inset:0;background:linear-gradient(180deg,#2a6fb8 0%,#4b8cc9 30%,#3a6f92 55%,#2f5a3e 80%,#274a33 100%)}
.brand{position:absolute;left:120px;top:14px;color:var(--white);font-weight:600;font-size:19px;letter-spacing:1.5px;line-height:22px;text-align:center}
.menu a{position:absolute;top:24px;color:var(--white);text-decoration:none;font-size:13px;font-weight:700;letter-spacing:.4px;white-space:nowrap}
.menu a.active{border-bottom:2px solid var(--white);padding-bottom:12px}
.nav-phone{position:absolute;left:940px;top:22px;font-size:15px;font-weight:700;display:flex;align-items:center;gap:6px;color:var(--white)}
.hero-name{position:absolute;top:190px;left:0;width:1200px;text-align:center;color:var(--white);font-weight:300;font-size:54px;letter-spacing:6px}
.hero-tag{position:absolute;color:var(--white);text-align:center;font-size:21px;line-height:29px;width:470px}
.hero-tag b{font-weight:800}

/* intro */
.h2{position:absolute;color:var(--blue);font-weight:700;font-size:30px;text-align:center}
.h2::after{content:"";display:block;width:70px;height:2px;background:var(--blue);margin:10px auto 0}
.para{position:absolute;font-size:16px;line-height:29px;text-align:center;color:var(--text)}
.para.sm{font-size:14.5px;line-height:26px}
.art{position:absolute;border-radius:6px}

/* why us */
.why{position:absolute;left:0;top:1358px;width:1200px;height:720px;background:linear-gradient(180deg,#f4f7fb 0%,#eef2f7 55%,#dfe6ee 100%)}
.kicker{position:absolute;width:1200px;text-align:center;font-size:13px;letter-spacing:2px;color:var(--muted)}
.card{position:absolute;width:342px;height:110px;border:2px solid #d6e3f0;border-radius:55px;background:rgba(255,255,255,.7)}
.card h3{position:absolute;font-size:16px;font-weight:800;color:var(--ink)}
.card p{position:absolute;font-size:12px;line-height:20px;color:var(--muted)}
.card .ic{position:absolute;top:9px;width:92px;height:92px;border-radius:50%;border:3px solid var(--blue);background:var(--white)}
.card.left h3,.card.left p{right:124px;text-align:right}
.card.left .ic{right:6px}
.card.right h3,.card.right p{left:124px}
.card.right .ic{left:6px}

/* services */
.svc h3{position:absolute;font-size:24px;font-weight:600;color:var(--ink);text-align:center;letter-spacing:.3px}
.svc p{position:absolute;font-size:14.5px;line-height:24px;text-align:center;color:var(--text)}
.dot{position:absolute;width:14px;height:14px;border-radius:50%;border:3px solid var(--blue);background:var(--white)}

/* contact */
.contact{position:absolute;left:0;top:3542px;width:1200px;height:600px}
.field{position:absolute;border:2px solid #c6cdd5;border-radius:20px;font-size:13px;color:#7b848e;padding:10px 20px}
.ci{position:absolute;display:flex;gap:14px;color:var(--white);font-weight:700;font-size:17px;line-height:28px}
.ci .b{width:36px;height:36px;border-radius:50%;background:var(--white);flex:none;display:flex;align-items:center;justify-content:center}

/* footer */
.footer{position:absolute;left:0;top:4080px;width:1200px;height:435px;background:var(--black);color:var(--white)}
.fbrand{position:absolute;left:150px;top:145px;font-size:19px;font-weight:600;letter-spacing:1.5px;line-height:22px;text-align:center}
.fcol{position:absolute;top:140px;padding-left:20px;border-left:2px solid var(--white)}
.fcol h4{font-size:14px;font-weight:800;letter-spacing:.5px;margin-top:-2px}
.fcol ul{list-style:none;margin-top:14px;font-size:14px;line-height:26px;color:#d8dde2}
.fi{width:24px;height:24px;border-radius:50%;background:#fff;flex:none;display:flex;align-items:center;justify-content:center}
.copy{position:absolute;bottom:20px;width:1200px;text-align:center;font-size:12px;color:#9aa3ac}
</style>
</head>
<body>

<!-- HERO -->
<header class="hero">
  <div class="hero-photo" role="img" aria-label="Photograph of misty blue mountain ridges and forested valley"></div>
  <div class="brand">BRAMWELL HOLLOW<br>GROUP</div>
  <nav class="menu">
    <a class="active" style="left:382px">HOME</a>
    <a style="left:477px">ABOUT US</a>
    <a style="left:600px">SERVICES</a>
    <a style="left:717px">FAQS</a>
    <a style="left:806px">CONTACT US</a>
  </nav>
  <div class="nav-phone">
    <svg width="17" height="17" viewBox="0 0 24 24"><path fill="#fff" d="M6.6 10.8a15.1 15.1 0 006.6 6.6l2.2-2.2c.3-.3.7-.4 1-.2 1.1.4 2.3.6 3.6.6.6 0 1 .4 1 1V20c0 .6-.4 1-1 1A17 17 0 013 4c0-.6.4-1 1-1h3.5c.6 0 1 .4 1 1 0 1.3.2 2.5.6 3.6.1.3 0 .7-.2 1z"/></svg>
    (555) 302-8146
  </div>
  <div class="hero-name">BRAMWELL HOLLOW</div>
  <svg class="abs" style="left:370px;top:345px" width="460" height="100" viewBox="0 0 460 100">
    <path d="M235 0v40q0 12-12 12H18q-10 0-10 10v36M240 0v40q0 12 12 12h190q10 0 10 10v30" fill="none" stroke="#fff" stroke-width="3"/>
    <circle cx="10" cy="96" r="5" fill="#fff" stroke="#1b74c9" stroke-width="3"/>
    <circle cx="450" cy="90" r="5" fill="#fff" stroke="#1b74c9" stroke-width="3"/>
  </svg>
  <div class="hero-tag" style="left:133px;top:464px">PERSONALIZED FINANCIAL ADVICE TO<br><b>HELP YOU ACHIEVE YOUR GOALS</b></div>
  <div class="hero-tag" style="left:606px;top:462px">PROFESSIONAL MANAGEMENT TO<br><b>MAKE YOUR MONEY WORK FOR YOU</b></div>
  <svg class="abs" style="left:0;top:480px" width="1200" height="170" viewBox="0 0 1200 170">
    <path d="M0 40Q600 250 1200 30V170H0z" fill="#fff"/>
    <path d="M0 40Q600 250 1200 30" fill="none" stroke="#1b74c9" stroke-width="6"/>
    <path d="M603 86l13 12 13-12" fill="none" stroke="#fff" stroke-width="4"/>
  </svg>
</header>

<!-- WHO WE ARE / SERVE -->
<section>
  <div class="h2" style="left:150px;top:700px;width:400px">WHO WE ARE</div>
  <div class="h2" style="left:645px;top:700px;width:400px">WHO WE SERVE</div>
  <p class="para" style="left:140px;top:765px;width:420px">Bramwell Hollow Group is an investment advisory firm committed to serving as fiduciary to our clients. We always act in the best interests of our clients, including putting your interests ahead of our own.</p>
  <p class="para sm" style="left:635px;top:765px;width:420px">Bramwell Hollow Group is for investors looking for the attention and personalization of services typically reserved for ultra high net worth (UHNW) investors. Our founder served UHNW clients at Halvorsen Trust, Meridian Ridge Partners</p>
  <svg class="abs" style="left:380px;top:875px" width="430" height="100" viewBox="0 0 430 100"><path d="M20 0v40q0 10 10 10h180q10 0 10 10v40M410 0v40q0 10-10 10H230q-10 0-10 10" fill="none" stroke="#c9d6e3" stroke-width="2"/></svg>
  <div class="art" style="left:245px;top:950px;width:736px;height:276px;background:linear-gradient(180deg,#ffffff 0%,#e7eff8 100%)" role="img" aria-label="Line illustration of two business people among charts, calendars, documents and office icons"></div>
  <div class="btn" style="left:512px;top:1265px;width:176px;height:47px">LEARN MORE</div>
</section>

<!-- WHY US -->
<section class="why">
  <svg class="abs" style="left:0;top:560px" width="1200" height="160" viewBox="0 0 1200 160">
    <path d="M0 90Q600 -20 1200 90V160H0z" fill="#fff"/>
    <path d="M0 90Q600 -20 1200 90" fill="none" stroke="#1b74c9" stroke-width="6"/>
  </svg>
  <div class="kicker" style="top:56px">WHY US?</div>
  <div class="h2" style="left:400px;top:78px;width:400px;font-size:34px">WHY WE ARE</div>

  <div class="card left" style="left:109px;top:163px"><h3 style="top:24px">You Come First</h3><p style="top:50px;width:190px">We always act in the best interests of our clients</p>
    <div class="ic"><svg width="86" height="86" viewBox="0 0 86 86"><path d="M22 48l10-8 8 4 10-6 14 10-10 8-8-4-10 6z" fill="none" stroke="#1b74c9" stroke-width="2.5"/><circle cx="43" cy="28" r="7" fill="none" stroke="#1b74c9" stroke-width="2.5"/></svg></div></div>
  <div class="card right" style="left:764px;top:161px"><h3 style="top:20px">Personalized Services</h3><p style="top:48px;width:200px">We get to know you in order to serve your unique needs</p>
    <div class="ic"><svg width="86" height="86" viewBox="0 0 86 86"><circle cx="43" cy="40" r="12" fill="none" stroke="#1b74c9" stroke-width="2.5"/><circle cx="43" cy="40" r="4" fill="#1b74c9"/><path d="M25 62h36" stroke="#1b74c9" stroke-width="2.5"/></svg></div></div>
  <div class="card left" style="left:109px;top:385px"><h3 style="top:24px">Transparent Fees</h3><p style="top:50px;width:190px">You'll always know what you pay and how we get paid</p>
    <div class="ic"><svg width="86" height="86" viewBox="0 0 86 86"><rect x="22" y="26" width="42" height="28" rx="2" fill="none" stroke="#1b74c9" stroke-width="2.5"/><text x="43" y="45" text-anchor="middle" font-size="12" font-family="Nunito Sans,sans-serif" fill="#1b74c9" font-weight="700">FEE</text><path d="M18 60h50" stroke="#1b74c9" stroke-width="2.5"/></svg></div></div>
  <div class="card right" style="left:770px;top:383px"><h3 style="top:20px">We Give Back</h3><p style="top:48px;width:200px">We support and better our local communities</p>
    <div class="ic"><svg width="86" height="86" viewBox="0 0 86 86"><circle cx="45" cy="32" r="9" fill="none" stroke="#1b74c9" stroke-width="2.5"/><text x="45" y="36" text-anchor="middle" font-size="11" fill="#1b74c9" font-family="Nunito Sans,sans-serif" font-weight="700">$</text><path d="M20 54l14-4 14 4 16-8M20 62h40" fill="none" stroke="#1b74c9" stroke-width="2.5"/></svg></div></div>

  <svg class="abs" style="left:440px;top:162px" width="340" height="340" viewBox="0 0 340 340">
    <circle cx="170" cy="170" r="160" fill="none" stroke="#b9cde2" stroke-width="2"/>
    <circle cx="55" cy="48" r="5" fill="#fff" stroke="#1b74c9" stroke-width="2.5"/>
    <circle cx="285" cy="48" r="5" fill="#fff" stroke="#1b74c9" stroke-width="2.5"/>
    <circle cx="27" cy="230" r="5" fill="#fff" stroke="#1b74c9" stroke-width="2.5"/>
    <circle cx="321" cy="214" r="5" fill="#fff" stroke="#1b74c9" stroke-width="2.5"/>
  </svg>
  <div class="abs" style="left:470px;top:192px;width:280px;height:280px;border-radius:50%;background:radial-gradient(circle at 50% 40%,#4a9be3,#1b74c9 70%,#0f5aa8);" role="img" aria-label="Blue-tinted photograph of a city skyline and river"></div>
  <div class="btn" style="left:526px;top:539px;width:157px;height:44px;background:transparent">VIEW FAQ</div>
</section>

<!-- SERVICES -->
<section class="svc">
  <div class="kicker" style="top:2079px">WHAT WE DO</div>
  <div class="h2" style="left:400px;top:2100px;width:400px;font-size:34px">OUR SERVICES</div>
  <div class="abs" style="left:595px;top:2239px;width:2px;height:993px;background:#a9c4e0"></div>
  <div class="dot" style="left:589px;top:2232px"></div>
  <div class="dot" style="left:589px;top:2567px"></div>
  <div class="dot" style="left:589px;top:2904px"></div>
  <div class="dot" style="left:589px;top:3224px"></div>

  <div class="art" style="left:140px;top:2204px;width:430px;height:231px;background:linear-gradient(160deg,#ffffff,#e4eef8)" role="img" aria-label="Line illustration of financial planning documents, calculator, clock and growth arrows"></div>
  <h3 style="left:625px;top:2230px;width:400px">FINANCIAL PLANNING</h3>
  <p style="left:635px;top:2270px;width:390px">Lorem ipsum dolor sit amet, consectetur adipiscing elit, sed do eiusmod tempor incididunt ut labore et dolore magna aliqua. Ut enim ad minim veniam, quis nostrud exercitation ullamco laboris nisi ut aliqu</p>
  <div class="btn" style="left:762px;top:2386px;width:158px;height:42px">LEARN MORE</div>

  <h3 style="left:150px;top:2573px;width:400px">ASSET MANAGEMENT</h3>
  <p style="left:155px;top:2613px;width:390px">Lorem ipsum dolor sit amet, consectetur adipiscing elit, sed do eiusmod tempor incididunt ut labore et dolore magna aliqua. Ut enim ad minim veniam, quis nostrud exercitation ullamco laboris nisi ut aliqu</p>
  <div class="btn" style="left:284px;top:2735px;width:160px;height:42px">LEARN MORE</div>
  <div class="art" style="left:640px;top:2532px;width:402px;height:245px;background:linear-gradient(200deg,#ffffff,#e4eef8)" role="img" aria-label="Line illustration of asset management with clipboard, money bag, gears and charts"></div>

  <div class="art" style="left:100px;top:2864px;width:450px;height:219px;background:linear-gradient(160deg,#ffffff,#e4eef8)" role="img" aria-label="Line illustration of a laptop showing charts with a business person presenting"></div>
  <h3 style="left:645px;top:2900px;width:400px">PORTFOLIO OPTIMIZATION</h3>
  <p style="left:655px;top:2940px;width:390px">Lorem ipsum dolor sit amet, consectetur adipiscing elit, sed do eiusmod tempor incididunt ut labore et dolore magna aliqua. Ut enim ad minim veniam, quis nostrud exercitation ullamco laboris nisi ut aliqu</p>
  <div class="btn" style="left:776px;top:3058px;width:160px;height:42px">LEARN MORE</div>

  <h3 style="left:130px;top:3207px;width:400px">ALTERNATIVE INVESTMENTS</h3>
  <p style="left:140px;top:3247px;width:390px">Lorem ipsum dolor sit amet, consectetur adipiscing elit, sed do eiusmod tempor incididunt ut labore et dolore magna aliqua. Ut enim ad minim veniam, quis nostrud exercitation ullamco laboris nisi ut aliqu</p>
  <div class="btn" style="left:264px;top:3367px;width:160px;height:42px">LEARN MORE</div>
  <div class="art" style="left:620px;top:3180px;width:452px;height:236px;background:linear-gradient(200deg,#ffffff,#e4eef8)" role="img" aria-label="Hand-lettered investment illustration with savings, growth and return icons"></div>
</section>

<!-- CONTACT -->
<section class="contact">
  <div class="abs" style="inset:0;background:linear-gradient(180deg,#1e72c4 0%,#2d84d2 45%,#1a6ec2 100%)" role="img" aria-label="Blue-tinted photograph of a mountain range"></div>
  <div class="abs" style="left:136px;top:98px;color:#dce9f7;font-size:15px;letter-spacing:.5px">GET IN TOUCH</div>
  <div class="abs" style="left:136px;top:118px;color:var(--white);font-size:34px;font-weight:600">CONTACT US</div>
  <div class="ci" style="left:140px;top:210px"><span class="b"><svg width="18" height="18" viewBox="0 0 24 24"><path fill="#1b74c9" d="M12 2a7 7 0 00-7 7c0 5 7 13 7 13s7-8 7-13a7 7 0 00-7-7zm0 9.5A2.5 2.5 0 1112 6.5a2.5 2.5 0 010 5z"/></svg></span><span>2280 Larkspur Ln, Suite #214<br>Fernbrook, VA 20417</span></div>
  <div class="ci" style="left:140px;top:296px"><span class="b"><svg width="18" height="18" viewBox="0 0 24 24"><path fill="#1b74c9" d="M6.6 10.8a15.1 15.1 0 006.6 6.6l2.2-2.2c.3-.3.7-.4 1-.2 1.1.4 2.3.6 3.6.6.6 0 1 .4 1 1V20c0 .6-.4 1-1 1A17 17 0 013 4c0-.6.4-1 1-1h3.5c.6 0 1 .4 1 1 0 1.3.2 2.5.6 3.6.1.3 0 .7-.2 1z"/></svg></span><span>(555) 302-8146</span></div>
  <div class="abs" style="left:110px;top:352px;width:405px;height:112px;border-radius:6px;background:linear-gradient(180deg,rgba(140,195,232,.35),rgba(20,70,130,.45))" role="img" aria-label="Illustration of layered mountain peaks with a location marker"></div>
  <div class="abs" style="left:538px;top:88px;width:548px;height:373px;background:var(--white);border-top-right-radius:70px"></div>
  <div class="field" style="left:568px;top:140px;width:238px;height:38px">First Name</div>
  <div class="field" style="left:812px;top:140px;width:238px;height:38px">Last Name</div>
  <div class="field" style="left:568px;top:194px;width:238px;height:38px">Email address</div>
  <div class="field" style="left:812px;top:194px;width:238px;height:38px">Phone</div>
  <div class="field" style="left:572px;top:245px;width:478px;height:106px">Message</div>
  <div class="abs" style="left:576px;top:373px;width:172px;height:44px;border-radius:22px;background:var(--blue);color:var(--white);font-size:13px;font-weight:800;letter-spacing:.8px;display:flex;align-items:center;justify-content:center">SEND MESSAGE</div>
  <svg class="abs" style="left:0;top:490px" width="1200" height="110" viewBox="0 0 1200 110">
    <path d="M0 20Q600 140 1200 20V110H0z" fill="#050607"/>
    <path d="M0 20Q600 140 1200 20" fill="none" stroke="#fff" stroke-width="6"/>
  </svg>
</section>

<!-- FOOTER -->
<footer class="footer">
  <div class="fbrand">BRAMWELL HOLLOW<br>GROUP</div>
  <p class="abs" style="left:140px;top:212px;width:290px;font-size:12px;line-height:16px;color:#c6ccd2">Lorem ipsum dolor sit amet, consectetur adipiscing elit, sed do eiusmod tempor incididunt ut labore et dolore</p>
  <div class="fcol" style="left:482px"><h4>NAVIGATION</h4><ul><li>Home</li><li>About Us</li><li>Services</li><li>FAQ</li><li>Contact Us</li></ul></div>
  <div class="fcol" style="left:692px"><h4>CONTACT US</h4>
    <div style="display:flex;gap:12px;margin-top:14px;font-size:13px;line-height:19px;color:#d8dde2"><span class="fi"><svg width="13" height="13" viewBox="0 0 24 24"><path fill="#050607" d="M12 2a7 7 0 00-7 7c0 5 7 13 7 13s7-8 7-13a7 7 0 00-7-7zm0 9.5A2.5 2.5 0 1112 6.5a2.5 2.5 0 010 5z"/></svg></span><span>2280 Larkspur Ln, Suite #214<br>Fernbrook, VA 20417</span></div>
    <div style="display:flex;gap:12px;margin-top:18px;font-size:13px;line-height:24px;color:#d8dde2"><span class="fi"><svg width="13" height="13" viewBox="0 0 24 24"><path fill="#050607" d="M6.6 10.8a15.1 15.1 0 006.6 6.6l2.2-2.2c.3-.3.7-.4 1-.2 1.1.4 2.3.6 3.6.6.6 0 1 .4 1 1V20c0 .6-.4 1-1 1A17 17 0 013 4c0-.6.4-1 1-1h3.5c.6 0 1 .4 1 1 0 1.3.2 2.5.6 3.6.1.3 0 .7-.2 1z"/></svg></span><span>(555) 302-8146</span></div>
  </div>
  <div class="fcol" style="left:955px"><h4>FOLLOW US</h4><div style="width:32px;height:32px;border-radius:50%;background:#fff;margin-top:12px"></div></div>
  <div class="copy">© 2022 Bramwell Hollow Group All Rights Reserved</div>
</footer>

</body>
</html>
```